Speisekarten für ein Seerestaurant/Pizzeria
Zielgruppe
Wir sin ein Seerestaurant/Pizzeria in einem Ferien Ort
Aufgabenstellung
Wir brauchen Speisekarte in A4 und A5 Format und wichtig dass wir das Inhalt immer einfach bearbeiten können

```html
<!DOCTYPE html>
<html lang="de">
<head>
<meta charset="utf-8">
<title>Seeblick – Speisekarte</title>
<link href="https://fonts.googleapis.com/css2?family=Abel&family=Great+Vibes&family=Open+Sans:ital,wght@0,600;0,700;1,400;1,600&display=swap" rel="stylesheet">
<style>
:root{
  --canvas:#e3e4e6;
  --paper:#fbfbfc;
  --script:#3c6a8e;
  --ink:#2f3236;
  --muted:#55595e;
  --note:#3b5fa0;
  --wash:#cfe0ee;
  --lake-a:#8fb0d8;
  --lake-b:#6f8fa6;
  --wood:#7a5a44;
  --food-a:#5a4a40;
  --food-b:#a0704e;
}
*{margin:0;padding:0;box-sizing:border-box}
html,body{width:1200px;height:2296px;overflow:hidden;background:var(--canvas)}
body{position:relative;font-family:'Abel',sans-serif;color:var(--ink)}

.page{position:absolute;overflow:hidden;box-shadow:0 6px 18px rgba(0,0,0,.12)}
.page-photo{position:absolute;inset:0}
.panel{position:absolute;background:rgba(251,251,252,.94)}
.wash{position:absolute;background:var(--wash);opacity:.55;border-radius:46% 54% 40% 60% / 55% 40% 60% 45%}
.script{font-family:'Great Vibes',cursive;color:var(--script);font-weight:400;position:absolute;white-space:nowrap}

/* Cover */
.cover{left:280px;top:150px;width:640px;height:905px}
.cover .page-photo{background:linear-gradient(180deg,var(--lake-a) 0%,#b9cde3 35%,#6d8fae 60%,#8a9aa8 80%,var(--wood) 100%)}
.cover .panel{left:30px;top:32px;right:30px;bottom:27px}
.cover .welcome{left:0;right:0;top:36px;text-align:center;font-size:38px}
.cover .wash{left:80px;top:140px;width:420px;height:470px}
.cover .bird{position:absolute;left:232px;top:230px;width:140px;height:190px;background:linear-gradient(180deg,#d5dbe2,#9aa4ae);border-radius:8px}
.brand{position:absolute;left:0;right:0;top:418px;text-align:center;font-size:78px;color:#1e2226;letter-spacing:1px}
.tagline{position:absolute;left:0;right:0;text-align:center;font-size:22px;letter-spacing:4px;color:#2a2e33}
.tagline.one{top:528px}
.tagline.two{top:562px}
.address{position:absolute;left:0;right:0;text-align:center;font-size:12.5px;letter-spacing:1.5px;color:#2a2e33}
.address.one{top:746px}
.address.two{top:766px}

/* Spread */
.spread-left{left:40px;top:1250px;width:560px;height:792px}
.spread-right{left:600px;top:1250px;width:560px;height:792px}
.spread-left .page-photo{background:linear-gradient(100deg,#4e8aa0 0%,#9fb9cf 30%,#c2d2de 55%,#7f9aa9 80%,#5a7d8c 100%)}
.spread-right .page-photo{background:linear-gradient(120deg,#2f2c2c 0%,var(--food-a) 30%,#8a6a55 60%,var(--food-b) 85%,#3d3330 100%)}
.spread .panel{left:27px;top:28px;width:505px;height:739px}

.section-title{font-size:32px}
.col{position:absolute}
.item{margin-bottom:10px}
.item-row{display:flex;align-items:baseline;font-size:13px;letter-spacing:.3px;text-transform:uppercase}
.item-row .name{white-space:nowrap}
.item-row .name small{text-transform:none;font-size:13px}
.leader{flex:1;border-bottom:1px dotted #888;margin:0 4px;transform:translateY(-3px)}
.price{font-family:'Open Sans',sans-serif;font-weight:700;font-size:7.5px;white-space:nowrap;width:44px;text-align:left}
.price .sub{display:block;font-weight:400;font-size:6.5px}
.desc{font-family:'Open Sans',sans-serif;font-style:italic;font-size:7.5px;line-height:1.5;color:var(--muted);padding-right:48px}
.note{position:absolute;font-family:'Open Sans',sans-serif;font-style:italic;font-weight:600;font-size:8.5px;line-height:1.45;color:var(--note);text-align:center}
.note .cap{display:block;font-style:normal;font-weight:600;font-size:7px;letter-spacing:1px;text-transform:uppercase;opacity:.8}
.photo{position:absolute;border-radius:2px}
.kicker{position:absolute;font-family:'Open Sans',sans-serif;font-weight:700;font-size:12px;letter-spacing:3px;text-align:center;color:#222}
.kicker.small{font-size:8.5px;letter-spacing:2px;line-height:1.25}
</style>
</head>
<body>

<section class="page cover">
  <div class="page-photo" role="img" aria-label="Seeterrasse mit Blick auf den See, Palmen und Korbmöbel"></div>
  <div class="panel">
    <div class="wash" role="img" aria-label="Helle Landkarte des Sees als Hintergrundfläche"></div>
    <h2 class="script welcome">Herzlich Willkommen</h2>
    <div class="bird" role="img" aria-label="Zeichnung einer Möwe auf einem Holzpfahl"></div>
    <h1 class="brand">Seeblick</h1>
    <p class="tagline one">Seerestaurant</p>
    <p class="tagline two">MÖWENBUCHT – Seewil</p>
    <p class="address one">Uferweg 12 • 6390 Seewil</p>
    <p class="address two">seeblick-moewenbucht.ch</p>
  </div>
</section>

<section class="page spread spread-left">
  <div class="page-photo" role="img" aria-label="Seeufer mit Bergen und Promenade"></div>
  <div class="panel">
    <div class="wash" style="left:90px;top:120px;width:320px;height:280px" role="img" aria-label="Helle Landkarte des Sees als Hintergrundfläche"></div>

    <h2 class="script section-title" style="left:84px;top:28px">Suppen</h2>
    <div class="col" style="left:32px;top:84px;width:200px">
      <div class="item"><div class="item-row"><span class="name">Bouillon</span><span class="leader"></span><span class="price">CHF 10.50</span></div><p class="desc">mit Tortelloni</p></div>
      <div class="item"><div class="item-row"><span class="name">Gulaschsuppe</span><span class="leader"></span><span class="price"><span class="sub">kl. Portion</span>CHF 13.50<span class="sub">kl. Portion</span>CHF 20.50</span></div><p class="desc" style="margin-top:-28px">...die Echte – nach ungarischer Art</p></div>
      <div class="item" style="margin-top:26px"><div class="item-row"><span class="name">Minestrone</span><span class="leader"></span><span class="price">CHF 11.50</span></div></div>
      <div class="item"><div class="item-row"><span class="name">Tagessuppe</span><span class="leader"></span><span class="price">CHF 11.50</span></div><p class="desc">fragen Sie unser Personal</p></div>
    </div>

    <h2 class="script section-title" style="left:324px;top:28px">Salate</h2>
    <div class="col" style="left:270px;top:84px;width:200px">
      <div class="item"><div class="item-row"><span class="name">Burrata</span><span class="leader"></span><span class="price">CHF 10.50</span></div><p class="desc">italienischer Frischkäse, mit frischem Basilikum, extra natives Olivenöl, Balsamico Crema und Cherry Tomaten</p></div>
      <div class="item"><div class="item-row"><span class="name">Ceasar Salat</span><span class="leader"></span><span class="price">CHF 13.50</span></div><p class="desc">mit Speck, Croûtons und Parmigiano DOP</p></div>
      <div class="item"><div class="item-row"><span class="name">Gemischter Salat</span><span class="leader"></span><span class="price">CHF 20.50</span></div></div>
      <div class="item"><div class="item-row"><span class="name">Grüner Salat</span><span class="leader"></span><span class="price">CHF 11.50</span></div></div>
      <div class="item"><div class="item-row"><span class="name">Nüsslisalat</span><span class="leader"></span><span class="price">CHF 11.50</span></div><p class="desc">mit Speck, Brotcroûtons und Ei</p></div>
      <div class="item"><div class="item-row"><span class="name">Salat «Möwenbucht»</span><span class="leader"></span><span class="price">CHF 11.50</span></div><p class="desc">Eisberg Salat, Speck, Croutons, Parmigiano DOP und Pouletstreifen</p></div>
    </div>
    <p class="note" style="left:270px;top:336px;width:200px">Alle Salate sind mit hausgemachter Salatsauce Ihrer Wahl und frischem Pizzabrot</p>

    <div class="photo" style="left:32px;top:305px;width:137px;height:124px;background:linear-gradient(135deg,#c9a36a,#6b3b20)" role="img" aria-label="Gulaschsuppe mit Brot"></div>
    <div class="photo" style="left:32px;top:437px;width:137px;height:124px;background:linear-gradient(135deg,#e6c78a,#7a9a4a)" role="img" aria-label="Schnitzel mit Salat"></div>
    <div class="photo" style="left:32px;top:569px;width:137px;height:124px;background:linear-gradient(135deg,#f2d25a,#c4622e)" role="img" aria-label="Chicken-Fingers mit Pommes Frites"></div>

    <h2 class="script section-title" style="left:270px;top:388px">Hauptgerichte</h2>
    <div class="col" style="left:199px;top:442px;width:271px">
      <div class="item"><div class="item-row"><span class="name">Beefsteak Tartar</span><span class="leader"></span><span class="price"><span class="sub">Vorspeise</span>CHF 22.50<span class="sub">Hauptgang</span>CHF 32.50</span></div><p class="desc" style="margin-top:-26px">aus Schweizer-Qualitätsrindfleisch abgeschmeckt nach Ihrem Wunsch, serviert mit Toastbrot und Butter</p></div>
      <div class="item" style="margin-top:16px"><div class="item-row"><span class="name">Chicken-Fingers</span><span class="leader"></span><span class="price">CHF 26.50</span></div><p class="desc">hausgemachte, panierte Pouletstreifen, dazu sweet Chili-Sauce und Pommes Frites</p></div>
      <div class="item"><div class="item-row"><span class="name">Cordon Bleu</span><span class="leader"></span><span class="price">CHF 32.50</span></div><p class="desc">«das Klassische» vom Schwein, gefüllt mit Vorderschinken, Raclette und würzigem Gruyère serviert mit Pommes Frites und Gemüse</p></div>
      <div class="item"><div class="item-row"><span class="name">Gyros-Teller</span><span class="leader"></span><span class="price">CHF 30.50</span></div><p class="desc">mit Schweinefleisch serviert mit Salat-Bouquet, Tzatziki-Sauce und Pommes Frites</p></div>
      <div class="item"><div class="item-row"><span class="name">Wiener Schnitzel</span><span class="leader"></span><span class="price">CHF 35.50</span></div><p class="desc">vom Kalb mit Pommes Frites und Preiselbeeren</p></div>
    </div>
  </div>
</section>

<section class="page spread spread-right">
  <div class="page-photo" role="img" aria-label="Grillgerichte vom Smoker, unscharf im Hintergrund"></div>
  <div class="panel">
    <div class="wash" style="left:200px;top:300px;width:290px;height:280px" role="img" aria-label="Helle Landkarte des Sees als Hintergrundfläche"></div>

    <h2 class="script section-title" style="left:0;right:0;top:26px;text-align:center">Barbecue Spezialitäten</h2>
    <p class="kicker" style="left:0;right:0;top:72px">AUS DEM SMOKER</p>

    <div class="photo" style="left:32px;top:116px;width:136px;height:124px;background:linear-gradient(135deg,#b0603a,#3a2a22)" role="img" aria-label="BBQ Spare Ribs auf Holzbrett"></div>
    <div class="photo" style="left:32px;top:248px;width:136px;height:124px;background:linear-gradient(135deg,#e0b060,#8a3a22)" role="img" aria-label="Pulled Pork Burger mit Pommes"></div>

    <div class="col" style="left:201px;top:112px;width:270px">
      <div class="item"><div class="item-row"><span class="name">BBQ Spare Ribs</span><span class="leader"></span><span class="price">CHF 44.00</span></div><p class="desc">aus dem Smoker mit Cherry-Bomb Glasur serviert mit Pommes frites</p></div>
      <div class="item"><div class="item-row"><span class="name">Pulled Beef <small>Burger</small></span><span class="leader"></span><span class="price">CHF 31.50</span></div><p class="desc">Hausgemachte Bun, Pulled Beef (180g), BBQ-Sauce, Cheddar-Käse, Coleslaw (Kabissalat) und Jalapeno, serviert mit Pommes</p></div>
      <div class="item"><div class="item-row"><span class="name">Pulled Pork <small>Burger</small></span><span class="leader"></span><span class="price">CHF 28.50</span></div><p class="desc">Hausgemachte Bun, Pulled Pork (180g), BBQ-Sauce, Cheddar-Käse, Coleslaw (Kabissalat) und Jalapeno, serviert mit Pommes</p></div>
      <div class="item"><div class="item-row"><span class="name">Pulled Vegi <small>Burger</small></span><span class="leader"></span><span class="price">CHF 26.50</span></div><p class="desc">Hausgemachte Bun, BBQ-Sauce, Cheddar-Käse, Coleslaw (Kabissalat) und Jalapeno, serviert mit Pommes</p></div>
    </div>
    <p class="note" style="left:201px;top:378px;width:270px">Barbecue Gerichte werden 6-12 Stunden im Smoker gegart. Wir verwenden ausschliesslich Schweizer Fleisch und Bio Hickory Holz für das typische BBQ-Erlebnis und Rauch-Aroma.</p>

    <p class="kicker small" style="left:32px;width:200px;top:432px">UNSERE<br>GRILLEMPFEHLUNGEN</p>
    <h2 class="script section-title" style="left:24px;top:464px">Auf dem heissen Stein</h2>
    <div class="col" style="left:32px;top:514px;width:200px">
      <div class="item"><div class="item-row"><span class="name">Pouletbrust</span><span class="leader"></span><span class="price">CHF 30.50</span></div><p class="desc">200 g</p></div>
      <div class="item"><div class="item-row"><span class="name">Rindsfilet</span><span class="leader"></span><span class="price">CHF 46.50</span></div><p class="desc">200 g</p></div>
      <div class="item"><div class="item-row"><span class="name">Schweinesteak</span><span class="leader"></span><span class="price">CHF 30.50</span></div><p class="desc">200 g</p></div>
    </div>
    <p class="note" style="left:32px;top:636px;width:190px"><span class="cap">Beilage nach Wahl</span>Pommes Frites, Röstikroketten, oder Grillgemüse</p>
    <p class="note" style="left:32px;top:680px;width:190px"><span class="cap">Beilage nach Wahl</span>Pfefferrahmsauce, Champignonrahmsauce oder Kräuterbutter</p>

    <h2 class="script section-title" style="left:328px;top:464px">Pasta</h2>
    <div class="col" style="left:272px;top:514px;width:199px">
      <div class="item"><div class="item-row"><span class="name">Penne all'Arrabbiata</span><span class="leader"></span><span class="price">CHF 21.50</span></div><p class="desc">Tomatensauce, Peperoncini und Knoblauch</p></div>
      <div class="item"><div class="item-row"><span class="name">Spaghetti<br>alla Napoletana</span><span class="leader"></span><span class="price">CHF 20.50</span></div><p class="desc">Tomatensauce und frischem Basilikum</p></div>
      <div class="item"><div class="item-row"><span class="name">Spaghetti Carbonara</span><span class="leader"></span><span class="price">CHF 24.50</span></div><p class="desc">mit Speck, Parmesan, Rahm und Eigelb</p></div>
      <div class="item"><div class="item-row"><span class="name">Tagliatelle della Casa</span><span class="leader"></span><span class="price">CHF 26.50</span></div><p class="desc">mit Pouletstreifen und Peperoncini an einer Champignon-Rahmsauce</p></div>
    </div>
  </div>
</section>

</body>
</html>
```